New design of old website

We need a new design of our domain name reseller website.

kavirnodo.com

we would also like new design for Logo and all.

the site will be in English and portuguesse,

Domain

```html
<!DOCTYPE html>
<html lang="en">
<head>
<meta charset="utf-8">
<title>Kavirnodo — Domain Reseller</title>
<link href="https://fonts.googleapis.com/css2?family=Source+Sans+3:wght@400;600;700&display=swap" rel="stylesheet">
<style>
:root{
  --blue:#0a9be0;
  --blue-dark:#0680c4;
  --blue-soft:#5ab8d8;
  --green:#3aa312;
  --ink:#1b1b1b;
  --white:#ffffff;
  --footer:#434e57;
  --footer-deep:#2a3038;
  --footer-text:#c9d1d7;
  --line:#67727b;
  --input:#b9c7d1;
}
*{margin:0;padding:0;box-sizing:border-box}
html,body{width:1200px;height:1004px;overflow:hidden}
body{font-family:"Source Sans 3",sans-serif;background:var(--white);position:relative;color:var(--ink)}
.abs{position:absolute}

.header{left:0;top:0;width:1200px;height:104px;background:linear-gradient(#eceff1,#ffffff 60%)}
.utility{left:879px;top:0;width:151px;height:20px;background:#0f4f92;color:var(--white);font-size:12px;display:flex;align-items:center}
.utility .label{margin-left:26px;width:60px}
.utility .lang{width:17px;height:13px;margin-left:4px}
.lang-en{background:#2c3e8f}
.lang-pt{background:#1f8a3a}

.brand{left:170px;top:34px;display:flex;align-items:center;gap:8px;font-size:44px;font-weight:700;color:var(--blue);letter-spacing:1px}
.brand .dot{width:34px;height:34px;border-radius:50%;background:var(--blue)}

.nav{left:441px;top:40px;width:589px;height:38px;border-radius:5px;background:linear-gradient(var(--blue),var(--blue-dark));display:flex;align-items:center;color:var(--white);font-size:13px;overflow:hidden}
.nav .home{background:linear-gradient(#4cb81f,var(--green));height:100%;width:70px;display:flex;align-items:center;justify-content:center}
.nav .item{padding:0 14px}
.nav .sep{opacity:.9}

.hero{left:0;top:104px;width:1200px;height:438px;background:linear-gradient(90deg,#d6ecef 0%,#b9d2d6 30%,#6e7f74 45%,#a8b6a8 70%,#c9ccb2 100%)}
.why{left:666px;top:142px;width:364px;height:359px;background:rgba(90,184,216,.9);clip-path:polygon(40px 0,100% 0,100% 100%,0 100%,0 52px);color:var(--white);text-align:center}
.why h1{font-weight:400;font-size:21px;margin-top:22px}
.why h2{font-weight:400;font-size:12px;margin:24px 30px 0;line-height:16px}
.why p{font-size:11.7px;line-height:16.1px;text-align:justify;margin:20px 36px 0;color:#102330}
.why .more{position:absolute;left:118px;top:292px;width:128px;height:37px;border-radius:4px;background:linear-gradient(var(--blue),var(--blue-dark));font-size:13px;display:flex;align-items:center;justify-content:center}

.features{left:170px;top:563px;width:860px;height:134px;border-radius:5px;background:linear-gradient(#12a7e6,var(--blue-dark));display:flex;color:var(--white)}
.feature{position:relative;padding:14px 0 0 22px;border-right:1px solid rgba(255,255,255,.18)}
.feature:last-child{border-right:none}
.feature .head{display:flex;align-items:center;gap:14px;height:46px;font-size:16px}
.feature .icon{width:38px;height:38px;flex:none}
.feature p{font-size:12.5px;line-height:14.5px;margin-top:12px}

.footer{left:0;top:724px;width:1200px;height:209px;background:var(--footer);color:var(--footer-text)}
.footer h3{position:absolute;top:20px;font-weight:400;font-size:16px;color:var(--white)}
.menu{position:absolute;top:50px;left:169px;display:grid;grid-template-columns:86px 86px;column-gap:28px}
.menu a{display:block;font-size:12.5px;padding:6px 0 7px 15px;border-bottom:1px solid var(--line);position:relative;color:var(--footer-text);text-decoration:none}
.menu a:nth-last-child(-n+2){border-bottom:none}
.menu a::before{content:"";position:absolute;left:2px;top:12px;border:3px solid transparent;border-left-color:var(--blue)}
.menu a.active{color:var(--blue)}
.news p{position:absolute;left:452px;top:60px;font-size:12.5px;line-height:18px;width:300px}
.email{position:absolute;left:450px;top:112px;width:284px;height:31px;border-radius:4px;background:var(--input);color:#4a5661;font-size:13px;padding:7px 12px}
.submit{position:absolute;left:638px;top:154px;width:97px;height:30px;border-radius:4px;background:linear-gradient(var(--blue),var(--blue-dark));color:var(--white);font-size:12.5px;display:flex;align-items:center;justify-content:center}
.social{position:absolute;left:826px;top:56px}
.social div{display:flex;align-items:center;gap:10px;height:27px;margin-bottom:8.5px;font-size:12.5px}
.social span.sq{width:27px;height:27px;border-radius:3px;background:#2a76b7}
.bottom{left:0;top:933px;width:1200px;height:71px;background:var(--footer-deep)}
.bottom p{position:absolute;left:172px;top:16px;color:var(--blue);font-size:12px}
</style>
</head>
<body>
<header class="abs header">
  <div class="abs utility"><span class="label">Search</span><span class="lang lang-en" aria-label="English"></span><span class="lang lang-pt" aria-label="Português"></span></div>
  <div class="abs brand"><span class="dot"></span>Kavirnodo</div>
  <nav class="abs nav">
    <span class="home">HOME</span>
    <span class="item">WHY KAVIRNODO</span><span class="sep">|</span>
    <span class="item">PRODUCTS</span><span class="sep">|</span>
    <span class="item">SERVICES</span><span class="sep">|</span>
    <span class="item">RESELLER</span><span class="sep">|</span>
    <span class="item">CONTACT</span><span class="sep">|</span>
    <span class="item">LOGIN</span>
  </nav>
</header>

<section class="abs hero" role="img" aria-label="Photo of a person touching a world map surrounded by domain extension tags"></section>
<section class="abs why">
  <h1>WHY KAVIRNODO</h1>
  <h2>GIVE YOUR CUSTOMERS A CHOICE OF 250 TOP LEVEL DOMAINS (TLDS)</h2>
  <p>Kavirnodo is mainly focused the the latin american marked. Today Kavirnodo is the fastest growing .br registrar and today many of the world's largest registrars are using Kavirnodonic to register .br domain with or without local present. With the unique KavirnodoNIC registration engine, you can offer your customers more than 200 top-level domains (TLDs). It is ideal for companies wishing to go beyond the usual narrow range of TLDs and differentiate themselves from competitors by offering a much larger portfolio.</p>
  <span class="more">READ MORE</span>
</section>

<section class="abs features">
  <div class="feature" style="width:217px">
    <div class="head"><svg class="icon" viewBox="0 0 38 38"><path d="M19 3 L33 8 V18 C33 27 26 33 19 36 C12 33 5 27 5 18 V8 Z" fill="#1c7a2c" stroke="#fff" stroke-width="2"/><path d="M12 19 L17 24 L27 13" fill="none" stroke="#fff" stroke-width="3.5"/></svg>SECURITY</div>
    <p>Protecting your brand against<br>against Undesire association.</p>
  </div>
  <div class="feature" style="width:214px">
    <div class="head"><span class="icon" style="background:#1a1f26;border-radius:4px"></span>TLD EXPECILIST</div>
    <p>Providing a large portfolio for<br>Your clients.</p>
  </div>
  <div class="feature" style="width:211px">
    <div class="head"><span class="icon" style="background:#f1cf2b;border-radius:4px"></span>AUTOMATION</div>
    <p>Domain process Quick<br>and Reliable.</p>
  </div>
  <div class="feature" style="width:218px;padding-left:16px">
    <div class="head"><span class="icon" style="background:#1a1f26;border-radius:50%"></span>PERSONAL SERVICE</div>
    <p>Domain process Quick<br>and Reliable.</p>
  </div>
</section>

<footer class="abs footer">
  <h3 style="left:169px">MENU</h3>
  <div class="menu">
    <a class="active">Home</a><a>Services</a>
    <a>Why kavirnodo</a><a>Reseller</a>
    <a>Products</a><a>Contact</a>
  </div>
  <div class="news">
    <h3 style="left:452px">NEWS LETTER</h3>
    <p>SIgn up for Special Offers. Enter your Email address Below and active your daily News latter</p>
    <div class="email">Email Adress</div>
    <div class="submit">SUMBIT</div>
  </div>
  <h3 style="left:827px">FOLOW US ON</h3>
  <div class="social">
    <div><span class="sq"></span>Proconnect</div>
    <div><span class="sq"></span>Chatter</div>
    <div><span class="sq"></span>Circlebook</div>
    <div><span class="sq"></span>Searchplus</div>
  </div>
</footer>
<div class="abs bottom"><p>©2013 All Right Reserved By Kavirnodo</p></div>
</body>
</html>
```